Website for Plumbing Company, Mr. BoilBright

I need a 7-page fully HTML-coded website for my plumbing company, Mr. BoilBright. We specialize in installation, repair, and replacement of both gas and electric water heaters. Although we offer both tankless (on-demand) water heaters and standard (with tank) water heaters, most of our business is related to standard (with tank) water heaters in the USA market.

These are the pages I need:
1. Home page with sections such as About Us, Our Services, Why Choose Us, Testimonials, Location Map (Palm Beach County Florida), Quote Request Form, Join Our Newsletter, Mission Statement, etc.

2. Gas Water Heaters

3. Electric Water Heaters

4. Tankless Water Heaters

5. About Us

6. Contact Us

7. Privacy Policy, Terms & Conditions

Be sure to mention the following points:
1. Same-Day Service
2. Best Price Guarantee
3. 100% Satisfaction Rating
4. 15-Year Warranty on Water Heater & Parts
5. Lifetime Warranty on Workmanship
*All Warranties are Transferrable Upon Home Sale

Once design is selected and finalized, I need the website coded in a standard HTML/CSS and temporarily hosted on your development server so I can see the website functionality that is not observable from screenshots, such as section animations, etc. Once those details are finalized, I will move the source code to my server and complete the project.

Target Market(s)

Residential Home Owners and Business Owners

Industry/Entity Type

Plumbing, Home Services, Remodeling, Construction

Coding

Coded - Design and coding required

Number of Pages Required

5+ page

Colors
0054AA
0677BA
7BADD7
CADEEF
E8F1F8
FFC000
F8CF3A
FAE287
FDF2CF
FEFAEE
EE7325
F08F49
F5BC92
FAE3D3
FDF4ED

Requirements
Must have
• Clean, colorful, and professional

```html
<!DOCTYPE html>
<html lang="en">
<head>
<meta charset="utf-8">
<title>Electric Water Heaters – Mr. BoilBright</title>
<link href="https://fonts.googleapis.com/css2?family=Plus+Jakarta+Sans:wght@400;500;600;700;800&family=DM+Sans:wght@400;500;600&display=swap" rel="stylesheet">
<style>
:root{
  --navy:#0c1d5e;
  --ink:#0b1a4a;
  --dark:#0a1230;
  --blue:#1877ee;
  --accent-blue:#2356c5;
  --yellow:#ffc800;
  --yellow-soft:#fdf2cf;
  --text:#5b6170;
  --line:#e4e7ee;
  --row:#f0f1f4;
  --white:#fff;
}
*{margin:0;padding:0;box-sizing:border-box}
html,body{width:1200px;height:3569px;overflow:hidden}
body{font-family:"DM Sans",sans-serif;color:var(--text);background:var(--white);position:relative}
.abs{position:absolute}
h1,h2,h3,h4,.hd{font-family:"Plus Jakarta Sans",sans-serif;color:var(--ink)}
/* top bar */
.topbar{left:0;top:0;width:1200px;height:36px;background:var(--dark);color:#e8ebf3;font-size:12px;display:flex;align-items:center;justify-content:space-between;padding:0 60px}
.topbar .area{display:flex;align-items:center;gap:8px}
.topbar .dot{width:14px;height:14px;border-radius:50%;background:var(--yellow)}
.topbar .links{display:flex;gap:26px}
/* header */
.brand{left:60px;top:48px;display:flex;align-items:center;gap:8px}
.brand .mark{width:34px;height:34px;border-radius:50%;background:var(--blue)}
.brand span{font-family:"Plus Jakarta Sans",sans-serif;font-weight:800;font-size:17px;color:var(--blue)}
.search{left:247px;top:61px;width:233px;height:36px;border:1px solid #dcdfe6;border-radius:2px}
.search svg{position:absolute;right:10px;top:10px}
.contact{top:58px;display:flex;align-items:center;gap:12px}
.contact .ic{width:42px;height:42px;border-radius:50%;background:var(--yellow);display:flex;align-items:center;justify-content:center}
.contact small{display:block;font-size:11px;color:#8a90a0}
.contact b{font-size:14px;color:var(--ink);font-weight:600}
/* nav */
.nav{left:60px;top:122px;width:1082px;height:66px;background:var(--blue);display:flex;align-items:center;padding-left:30px;z-index:3}
.nav a{color:#fff;font-family:"Plus Jakarta Sans",sans-serif;font-weight:600;font-size:15px;text-decoration:none;display:flex;align-items:center}
.nav a+a::before{content:"";width:5px;height:5px;border-radius:50%;background:var(--yellow);margin:0 22px}
.nav a.on{color:var(--yellow)}
.nav .cta{position:absolute;right:0;top:0;height:66px;width:179px;background:var(--yellow);color:var(--ink);font-weight:700;font-size:14px;display:flex;align-items:center;justify-content:center;font-family:"Plus Jakarta Sans",sans-serif}
/* hero */
.hero{left:0;top:154px;width:1200px;height:334px;background:linear-gradient(90deg,#6f7c8c 0%,#3d4f6d 30%,#243e78 65%,#1d4ea6 100%)}
.hero-shade{left:0;top:154px;width:1200px;height:334px;background:rgba(10,30,80,.35)}
.hero h1{left:0;top:256px;width:1200px;text-align:center;color:#fff;font-size:39px;font-weight:700}
.hero-line{left:544px;top:315px;width:112px;height:4px;background:var(--yellow)}
.crumb{left:0;top:354px;width:1200px;display:flex;justify-content:center;gap:14px;align-items:center;font-size:18px;color:#fff}
.crumb .cur{color:var(--yellow);font-size:16px}
/* tags */
.tag{display:inline-flex;align-items:center;gap:6px;background:var(--yellow-soft);color:#e2a400;font-size:13px;font-weight:600;padding:6px 12px;text-transform:uppercase;font-family:"Plus Jakarta Sans",sans-serif}
/* intro */
.intro-tag{left:75px;top:594px}
.intro h2{font-size:38px;line-height:42px;font-weight:800}
.intro-h{left:75px;top:646px;width:580px}
.intro-p{left:75px;top:752px;width:540px;font-size:15.5px;line-height:22px}
.feat{display:flex;gap:14px;align-items:center;width:300px}
.feat .ci{width:36px;height:36px;border-radius:50%;background:var(--navy);flex:none;display:flex;align-items:center;justify-content:center}
.feat p{font-family:"Plus Jakarta Sans",sans-serif;font-weight:600;font-size:14.5px;color:var(--ink);line-height:19px}
.btn{display:flex;align-items:center;justify-content:center;font-family:"Plus Jakarta Sans",sans-serif;font-weight:700;font-size:14px;color:var(--ink)}
.btn-y{left:75px;top:990px;width:263px;height:47px;background:var(--yellow)}
.btn-o{left:349px;top:990px;width:210px;height:47px;border:1.5px solid var(--accent-blue);color:var(--ink)}
.note{left:77px;top:1052px;font-size:12.5px;color:#6c7280}
.ph{border:0}
.ph-big{left:776px;top:608px;width:345px;height:391px;background:linear-gradient(135deg,#b24a2a,#d9792f 40%,#7a8592 75%,#3a6bc0)}
.ph-small{left:705px;top:831px;width:189px;height:211px;background:linear-gradient(135deg,#555c66,#8b9199 50%,#3a3f48);outline:6px solid #fff}
/* section heads */
.center{left:0;width:1200px;text-align:center}
.sec-h{font-size:38px;font-weight:800}
.sec-p{font-size:15.5px;line-height:21px;width:520px;left:340px;text-align:center}
/* service cards */
.card{top:1371px;width:334px;height:165px;background:var(--navy);padding:30px 26px 0 62px;color:#dfe4f3}
.card.y{background:var(--yellow);color:var(--ink)}
.card .ci{position:absolute;left:10px;top:28px;width:44px;height:44px;border-radius:50%;background:var(--yellow);display:flex;align-items:center;justify-content:center}
.card.y .ci{background:var(--navy)}
.card h3{color:#fff;font-size:21px;line-height:23px;font-weight:700;margin-bottom:18px}
.card.y h3{color:var(--ink)}
.card p{font-size:11.5px;line-height:16.5px}
.bullets{top:1561px;left:78px;display:flex;gap:38px;font-family:"Plus Jakarta Sans",sans-serif;font-weight:600;font-size:11.5px;color:var(--ink)}
/* table */
.table{left:75px;top:1906px;width:1050px;height:427px}
.table .row{position:absolute;left:0;width:1050px}
.table .c{position:absolute;font-size:16px}
.th{top:0;height:86px;background:var(--row);border-bottom:3px solid #dfe2e8}
.th .c{font-family:"Plus Jakarta Sans",sans-serif;font-weight:700;font-size:20px;color:var(--ink)}
.tr .c.l{color:var(--ink)}
.tr .c{color:var(--accent-blue)}
.tr.g{background:var(--row)}
.tr.g .c{color:#6c7280}
/* faq */
.faq-img{left:83px;top:2464px;width:446px;height:616px;background:linear-gradient(160deg,#e9e6e0,#c9c2b5 45%,#6a5d4d 80%,#3a3a3a)}
.faq-tag{left:594px;top:2458px}
.faq-h{left:586px;top:2506px;font-size:42px;line-height:46px;font-weight:800}
.acc{left:590px;width:542px;height:57px;background:var(--accent-blue);color:#fff;font-family:"Plus Jakarta Sans",sans-serif;font-weight:700;font-size:17px;display:flex;align-items:center;justify-content:space-between;padding:0 22px 0 28px}
.acc-body{left:595px;top:2712px;width:525px;font-size:12px;line-height:21px;color:#5b6170}
/* footer */
.footer{left:0;top:3178px;width:1194px;height:391px;background:linear-gradient(110deg,#0a1433 0%,#0c1a45 55%,#11265a 100%)}
.fh{font-family:"Plus Jakarta Sans",sans-serif;color:#fff;font-weight:800;font-size:16px;text-transform:uppercase}
.fl{font-size:13px;color:#d5dae8;line-height:33px}
.fp{font-size:12.5px;color:#8b93aa;line-height:16px}
.soc{top:3429px;display:flex;gap:12px;left:50px}
.soc i{width:38px;height:38px;border-radius:50%;background:#fff;display:block}
.news{left:852px;top:3350px;width:280px;height:48px;background:#fff;display:flex;align-items:center;justify-content:space-between;padding:0 14px 0 20px;font-size:13px;color:#333}
.pay{top:3520px;display:flex;gap:7px;left:732px}
.pay i{width:51px;height:27px;border-radius:3px;display:block}
</style>
</head>
<body>

<div class="abs topbar">
  <div class="area"><span class="dot"></span>Serving Palm Beach County &amp; Surroundings</div>
  <div class="links"><span>Get Help</span><span>FAQ</span><span>My Account</span></div>
</div>

<div class="abs brand"><span class="mark"></span><span>Mr. BoilBright</span></div>
<div class="abs search"><svg width="16" height="16" viewBox="0 0 16 16" fill="none" stroke="#b8bcc6" stroke-width="1.5"><circle cx="7" cy="7" r="5"/><path d="M11 11l3.5 3.5"/></svg></div>

<div class="abs contact" style="left:516px">
  <div class="ic"><svg width="18" height="18" viewBox="0 0 24 24" fill="none" stroke="#0b1a4a" stroke-width="2"><rect x="3" y="5" width="18" height="14" rx="2"/><path d="M3 7l9 6 9-6"/></svg></div>
  <div><small>Email Us</small><b>hello@boilbright-mail.com</b></div>
</div>
<div class="abs contact" style="left:750px">
  <div class="ic"><svg width="18" height="18" viewBox="0 0 24 24" fill="#0b1a4a"><path d="M6.6 10.8a15 15 0 006.6 6.6l2.2-2.2a1 1 0 011-.25 11.4 11.4 0 003.6.57 1 1 0 011 1V20a1 1 0 01-1 1A17 17 0 013 4a1 1 0 011-1h3.5a1 1 0 011 1c0 1.25.2 2.45.57 3.57a1 1 0 01-.25 1z"/></svg></div>
  <div><small>Call us any time</small><b>+1 561-555-0148</b></div>
</div>
<div class="abs contact" style="left:962px">
  <div class="ic"><svg width="18" height="18" viewBox="0 0 24 24" fill="none" stroke="#0b1a4a" stroke-width="2"><path d="M12 21s-7-6.2-7-11.5A7 7 0 0119 9.5C19 14.8 12 21 12 21z"/><circle cx="12" cy="10" r="2.5"/></svg></div>
  <div><small>Locations</small><b>42 Harbor Lane, FL</b></div>
</div>

<div class="abs hero" role="img" aria-label="Technician checking an electrical panel with a tablet"></div>
<div class="abs hero-shade"></div>

<nav class="abs nav">
  <a>Home</a><a>About Us</a><a>Gas Water Heaters</a><a class="on">Electric Water Heaters</a><a>Tankless</a><a>Contact us</a>
  <span class="cta">Request a Call Back</span>
</nav>

<div class="hero"><h1 class="abs" style="left:0;top:256px;width:1200px;text-align:center;color:#fff;font-size:39px;font-weight:700">Electric Water Heaters</h1></div>
<div class="abs hero-line"></div>
<div class="abs crumb"><span>Home</span>
  <svg width="20" height="16" viewBox="0 0 20 16" fill="none" stroke="#ffc800" stroke-width="2.2"><path d="M2 2l6 6-6 6M10 2l6 6-6 6"/></svg>
  <span class="cur">Electric Water Heaters</span></div>

<!-- intro -->
<div class="abs intro-tag"><span class="tag">⚡ Electric Water Heater Specialists</span></div>
<div class="abs intro intro-h"><h2>Quiet, Reliable Electric Water Heaters Installed in One Day</h2></div>
<p class="abs intro-p">We install, repair, and replace standard (with tank) electric water heaters for Palm Beach County homeowners and businesses. Same-day service with unbeatable warranties.</p>

<div class="abs feat" style="left:73px;top:852px">
  <div class="ci"><svg width="18" height="18" viewBox="0 0 24 24" fill="none" stroke="#fff" stroke-width="2"><path d="M20 12a8 8 0 01-14 5.3M4 12a8 8 0 0114-5.3M18 3v4h-4M6 21v-4h4"/></svg></div>
  <p>Same-Day Replacement on Most Electric Tanks</p></div>
<div class="abs feat" style="left:373px;top:852px">
  <div class="ci"><svg width="16" height="16" viewBox="0 0 24 24" fill="none" stroke="#fff" stroke-width="2"><rect x="5" y="9" width="10" height="12" rx="1"/><path d="M9 9V5h10v12h-4"/></svg></div>
  <p>Best Price Guarantee on Comparable Systems</p></div>
<div class="abs feat" style="left:73px;top:905px">
  <div class="ci"><svg width="16" height="16" viewBox="0 0 24 24" fill="none" stroke="#fff" stroke-width="2"><path d="M12 3l8 3v6c0 5-3.5 8-8 9-4.5-1-8-4-8-9V6z"/><path d="M12 9v6M9 12h6"/></svg></div>
  <p>15-Year Warranty on Tank &amp; Parts</p></div>
<div class="abs feat" style="left:373px;top:905px">
  <div class="ci"><svg width="16" height="16" viewBox="0 0 24 24" fill="none" stroke="#fff" stroke-width="2"><path d="M12 3l8 3v6c0 5-3.5 8-8 9-4.5-1-8-4-8-9V6z"/><path d="M12 9v6M9 12h6"/></svg></div>
  <p>Lifetime Warranty on Our Workmanship</p></div>

<div class="abs btn btn-y">SCHEDULE ELECTRIC SERVICE</div>
<div class="abs btn btn-o">SEE ELECTRIC BENEFITS</div>
<p class="abs note">*All warranties are transferrable upon home sale – 100% satisfaction rating</p>

<div class="abs ph ph-big" role="img" aria-label="Plumber in hard hat connecting pipes to a water heater"></div>
<div class="abs ph ph-small" role="img" aria-label="Technician tightening a fitting under a tank"></div>

<!-- services -->
<div class="abs center" style="top:1187px"><span class="tag">⚡ Services</span></div>
<h2 class="abs center sec-h" style="top:1222px">Electric Water Heaters</h2>
<p class="abs sec-p" style="top:1287px">Expert installation and repair of high-efficiency gas water heating systems for your home.</p>

<div class="abs card" style="left:75px">
  <div class="ci"><svg width="20" height="20" viewBox="0 0 24 24" fill="none" stroke="#0c1d5e" stroke-width="2"><path d="M4 21V9l8-5 8 5v12M9 21v-6h6v6M8 11h2M14 11h2"/></svg></div>
  <h3>Perfect for Condos &amp; Townhomes</h3>
  <p>No gas line or vent required. Ideal for interior closets, garages, and utility rooms in multi-family buildings.</p>
</div>
<div class="abs card y" style="left:434px">
  <div class="ci"><svg width="22" height="22" viewBox="0 0 24 24" fill="#ffc800"><path d="M10 3l1.8 5.2L17 10l-5.2 1.8L10 17l-1.8-5.2L3 10l5.2-1.8zM18 14l.9 2.1L21 17l-2.1.9L18 20l-.9-2.1L15 17l2.1-.9z"/></svg></div>
  <h3>Clean &amp; Low-Maintenance</h3>
  <p>No combustion exhaust, burner cleaning, or gas leak concerns. Simple electrical connections and thermostats.</p>
</div>
<div class="abs card" style="left:791px">
  <div class="ci"><svg width="20" height="20" viewBox="0 0 24 24" fill="none" stroke="#0c1d5e" stroke-width="2"><path d="M12 3l8 3v6c0 5-3.5 8-8 9-4.5-1-8-4-8-9V6z"/><path d="M8.5 12l2.5 2.5 4.5-5"/></svg></div>
  <h3>Backed by Long Warranties</h3>
  <p>15-year tank &amp; parts coverage plus lifetime workmanship warranty, fully transferrable to a new owner if you sell.</p>
</div>
<div class="abs bullets"><span>40–80 gallon electric tanks</span><span>High-efficiency models available</span><span>Code-compliant drain pans &amp; shutoffs</span><span>Old tank haul-away included</span></div>

<!-- comparison -->
<div class="abs center" style="top:1710px"><span class="tag">⚡ Electric Water Heater Specialists</span></div>
<h2 class="abs center sec-h" style="top:1760px">Electric vs. Gas vs. Tankless</h2>
<p class="abs sec-p" style="top:1829px">Not sure if electric is right for you? Here's how it compares to other common options we install.</p>

<div class="abs table">
  <div class="row th"><span class="c" style="left:40px;top:42px">Feature</span><span class="c" style="left:299px;top:16px">Electric (Tank)</span><span class="c" style="left:586px;top:16px">Gas (Tank)</span><span class="c" style="left:845px;top:16px">Tankless</span></div>
  <div class="row tr" style="top:86px;height:83px"><span class="c l" style="left:40px;top:42px">Upfront Cost</span><span class="c" style="left:299px;top:18px">Lowest  for most homes</span><span class="c" style="left:586px;top:18px">Gas (Tank)</span><span class="c" style="left:845px;top:18px">Tankless</span></div>
  <div class="row tr g" style="top:169px;height:80px"><span class="c" style="left:40px;top:40px">Upfront Cost</span><span class="c" style="left:299px;top:16px">10–15 years</span><span class="c" style="left:586px;top:16px">10–15 years</span><span class="c" style="left:845px;top:16px">10–15 years</span></div>
  <div class="row tr" style="top:249px;height:83px"><span class="c l" style="left:40px;top:44px">Upfront Cost</span><span class="c" style="left:299px;top:19px">Good with high-efficiency models</span><span class="c" style="left:586px;top:19px">Very good</span><span class="c" style="left:845px;top:19px">Best</span></div>
  <div class="row tr g" style="top:332px;height:95px"><span class="c" style="left:40px;top:46px">Upfront Cost</span><span class="c" style="left:299px;top:20px">Lowest  for most homes</span><span class="c" style="left:586px;top:20px">Gas (Tank)</span><span class="c" style="left:845px;top:20px">Tankless</span></div>
</div>

<!-- faq -->
<div class="abs faq-img" role="img" aria-label="Plumber fitting an orange hose to a wall-mounted electric water heater"></div>
<div class="abs faq-tag"><span class="tag">⚡ FAQ</span></div>
<h2 class="abs faq-h">Uilt For Comfort.<br>Backed By Trust.</h2>

<div class="abs acc" style="top:2632px">What Are The Main Types Of Fishing Equipments?<svg width="16" height="10" viewBox="0 0 16 10" fill="none" stroke="#fff" stroke-width="2"><path d="M2 8l6-6 6 6"/></svg></div>
<p class="abs acc-body">Lorem Ipsum Dolor Sit Amet, Consectetur Adipiscing Elit, Sed Do Eiusmod Tempor Incididunt Ut Labore Et Dolore Magna Aliqua. Ut Enim Ad Minim Veniam, Quis Nostrud Exercitation Ullaco Laboris Nisi</p>
<div class="abs acc" style="top:2793px">What Are The Main Types Of Fishing Equipments?<svg width="16" height="10" viewBox="0 0 16 10" fill="none" stroke="#fff" stroke-width="2"><path d="M2 2l6 6 6-6"/></svg></div>
<div class="abs acc" style="top:2868px">What Are The Main Types Of Fishing Equipments?<svg width="16" height="10" viewBox="0 0 16 10" fill="none" stroke="#fff" stroke-width="2"><path d="M2 2l6 6 6-6"/></svg></div>
<div class="abs acc" style="top:2943px">What Are The Main Types Of Fishing Equipments?<svg width="16" height="10" viewBox="0 0 16 10" fill="none" stroke="#fff" stroke-width="2"><path d="M2 2l6 6 6-6"/></svg></div>

<!-- footer -->
<footer class="abs footer"></footer>
<h4 class="abs fh" style="left:51px;top:3238px;font-size:20px">Help Customers</h4>
<p class="abs fp" style="left:49px;top:3284px;width:230px">Find a location nearest you to reduce shipping costs and make shopping easier.</p>
<p class="abs" style="left:51px;top:3348px;color:#fff;font-family:'Plus Jakarta Sans',sans-serif;font-weight:600;font-size:20px;line-height:26px">+1 (561) 555-0172<br><span style="font-size:19px">service@boilbright-mail.com</span></p>
<div class="abs soc"><i></i><i></i><i></i><i></i></div>

<h4 class="abs fh" style="left:355px;top:3238px">Our Company</h4>
<div class="abs fl" style="left:357px;top:3270px">About us<br>Contact us<br>Our Store<br>FAQ<br>Store location</div>

<h4 class="abs fh" style="left:578px;top:3238px">Services</h4>
<div class="abs fl" style="left:580px;top:3270px">Gas Water Heaters<br>Electric Water Heaters<br>Tankless Water Heaters</div>

<h4 class="abs fh" style="left:850px;top:3238px">Sign up to Newsletter</h4>
<p class="abs fp" style="left:852px;top:3280px;width:270px">Sign up for 10% off your first purchase and free shipping. Updates information on Sales and Offers.</p>
<div class="abs news">Enter your<svg width="20" height="20" viewBox="0 0 24 24" fill="#0b1a4a"><path d="M3 4l18 0-10 17-2-7z"/></svg></div>
<p class="abs fp" style="left:852px;top:3438px;width:280px;color:#d5dae8">***By entering the e-mail you accept the terms and conditions and the privacy policy.</p>

<p class="abs" style="left:51px;top:3525px;font-size:13.5px;color:#d5dae8">Copyright © 2025 Mr. BoilBright - All Rights Reserved.</p>
<div class="abs pay" aria-label="Accepted payment methods">
  <i style="background:#2e8fd6"></i><i style="background:#f5a9c4"></i><i style="background:#1b4fa8"></i><i style="background:#2a2a2a"></i><i style="background:#f4d22a"></i><i style="background:#1a2a8c"></i><i style="background:#1d6fd0"></i>
</div>

</body>
</html>
```